Pharmacy window design

WINDOW DIMENSIONS

4ft 8 1/2" WIDE
7ft 4 1/2" HIGH

i need a window sticker for 4 windows for the outside of a pharmacy. see attached examples. name of the pharmacy is Vita Corner

we would prefer to display products on the window signs eg. Baby care products, medicines. vitamins. fitness. veterinary, Health/ beauty etc.

Target Market(s)

Locals and Tourists

Industry/Entity Type

Pharmacy

```html
<!DOCTYPE html>
<html lang="en">
<head>
<meta charset="utf-8">
<title>Vita Corner – Window Banners</title>
<link rel="stylesheet" href="https://fonts.googleapis.com/css2?family=Oswald:wght@400;500;600&family=Open+Sans:wght@700&family=Fira+Sans:wght@600&display=swap">
<style>
  :root {
    --stage: #464646;
    --navy: #333f8f;
    --navy-dark: #2a3579;
    --green: #7dc242;
    --green-soft: #86c653;
    --white: #ffffff;
    --label: #f2f2f2;
    --photo-warm: #f3d9dc;
    --photo-neutral: #e6e2dc;
    --photo-teal: #cfe6e3;
    --photo-multi: #e9b67a;
    --photo-red: #e8c2c6;
    --photo-dark: #3b3e45;
    --photo-device: #f1f1f1;
    --photo-icons: #3fa69a;
    --photo-kit: #d63a35;
  }
  * { box-sizing: border-box; margin: 0; padding: 0; }
  html, body { width: 1200px; height: 1200px; overflow: hidden; background: var(--stage); }
  .canvas { position: relative; width: 1200px; height: 1200px; }

  .banner { position: absolute; width: 287px; height: 502px; overflow: hidden; }
  .banner-label {
    position: absolute; width: 300px; text-align: center;
    font-family: "Fira Sans", sans-serif; font-weight: 600; font-size: 32px; color: var(--label);
  }
  .abs { position: absolute; }
  .photo { position: absolute; border-radius: 3px; }

  .brand {
    position: absolute; display: flex; align-items: center; gap: 7px;
    font-family: "Oswald", sans-serif; font-weight: 500; color: var(--navy); white-space: nowrap;
  }
  .brand-dot { border-radius: 50%; background: var(--green); flex: none; }

  /* banner 1 */
  .banner-products { left: 205px; top: 32px; background: var(--white); }
  .product-tag {
    position: absolute; width: 122px; height: 29px; background: var(--navy);
    border: 1px solid #5563b0; border-radius: 3px;
    color: var(--green); font-family: "Oswald", sans-serif; font-weight: 500; font-size: 16px;
    display: flex; align-items: center; justify-content: center; white-space: nowrap;
  }
  .product-tag.long { font-size: 14.5px; }

  /* banner 2 */
  .banner-services { left: 695px; top: 32px; background: var(--navy); }
  .top-stripe { left: 0; top: 0; width: 287px; height: 8px; background: linear-gradient(90deg, var(--navy) 0 51%, var(--green) 51% 100%); }
  .header { left: 0; width: 100%; height: 82px; background: var(--white); }
  .service-list { left: 12px; top: 86px; list-style: none; }
  .service-list li, .extras li {
    display: flex; align-items: center; gap: 5px;
    font-family: "Oswald", sans-serif; font-weight: 500; color: var(--white); white-space: nowrap;
  }
  .service-list li { font-size: 14.5px; height: 30px; }
  .tick { width: 8px; height: 8px; flex: none; }
  .octagon { clip-path: polygon(30% 0, 70% 0, 100% 22%, 100% 78%, 70% 100%, 30% 100%, 0 78%, 0 22%); }
  .also-title {
    left: 130px; top: 279px; font-family: "Oswald", sans-serif; font-weight: 500; font-size: 23px;
    color: var(--green); border-bottom: 1.5px solid var(--green); line-height: 1.05; padding-bottom: 1px;
  }
  .extras { left: 140px; top: 306px; list-style: none; }
  .extras li { font-size: 17px; height: 25px; }
  .open-small { left: 120px; top: 384px; font-family: "Oswald", sans-serif; font-weight: 500; font-size: 18px; color: var(--green); }
  .hours-small { left: 102px; top: 408px; font-family: "Oswald", sans-serif; font-weight: 500; font-size: 15px; line-height: 18px; color: var(--white); }
  .insurance-band {
    left: 117px; top: 460px; width: 170px; height: 42px; background: var(--green);
    display: flex; align-items: center; justify-content: center;
    font-family: "Oswald", sans-serif; font-size: 10.5px; color: var(--white); white-space: nowrap;
  }

  /* banner 3 */
  .banner-hours { left: 209px; top: 604px; width: 288px; height: 504px; background: var(--navy); }
  .plus-ring { left: 70px; top: 114px; }
  .open-band {
    left: 0; top: 282px; width: 100%; height: 40px; background: var(--green);
    display: flex; align-items: center; justify-content: center;
    font-family: "Oswald", sans-serif; font-weight: 500; font-size: 33px; color: var(--navy-dark);
  }
  .hours-large {
    left: 0; top: 332px; width: 100%; text-align: center;
    font-family: "Oswald", sans-serif; font-weight: 500; font-size: 33px; line-height: 38px; color: var(--white);
  }
  .insurance-footer {
    left: 0; top: 462px; width: 100%; height: 42px; background: var(--white);
    border-top: 3px solid var(--green);
    display: flex; align-items: center; justify-content: center;
    font-family: "Open Sans", sans-serif; font-weight: 700; font-size: 14px; color: var(--green); letter-spacing: -0.3px;
  }

  /* banner 4 */
  .banner-brand { left: 696px; top: 606px; background: var(--green); }
  .icon-field { left: 0; top: 0; width: 100%; height: 100%; background: var(--green-soft); }
</style>
</head>
<body>
<div class="canvas">

  <!-- Product banner -->
  <section class="banner banner-products">
    <div class="brand" style="left:16px; top:12px; font-size:17px;"><span class="brand-dot" style="width:12px;height:12px;"></span>Vita Corner</div>
    <div class="photo" role="img" aria-label="Baby care products: bath toys, lotions and towels" style="left:147px; top:0; width:139px; height:116px; background:linear-gradient(135deg,var(--photo-warm),#fbeef0);"></div>
    <div class="product-tag long" style="left:17px; top:59px;">Baby Care Products</div>

    <div class="photo" role="img" aria-label="Row of cosmetic and beauty product bottles" style="left:7px; top:124px; width:138px; height:64px; background:linear-gradient(90deg,var(--photo-neutral),#f4efe9);"></div>
    <div class="product-tag" style="left:154px; top:144px;">Health/ Beauty</div>

    <div class="photo" role="img" aria-label="Veterinary medicine box" style="left:151px; top:200px; width:122px; height:72px; background:linear-gradient(135deg,#f4f4f4,var(--photo-teal));"></div>
    <div class="product-tag" style="left:14px; top:227px;">Veterinary</div>

    <div class="photo" role="img" aria-label="Colourful vitamin capsules" style="left:11px; top:272px; width:128px; height:80px; background:linear-gradient(135deg,var(--photo-multi),#d95a4a 60%,#6cb85a);"></div>
    <div class="product-tag" style="left:150px; top:297px;">Vitamins</div>

    <div class="photo" role="img" aria-label="Blister packs of medicine tablets" style="left:159px; top:352px; width:122px; height:56px; background:linear-gradient(135deg,var(--photo-red),#d5ece6);"></div>
    <div class="product-tag" style="left:21px; top:370px;">Medicines</div>

    <div class="photo" role="img" aria-label="Tub of protein powder with scoop" style="left:51px; top:408px; width:64px; height:80px; background:linear-gradient(180deg,var(--photo-dark),#5a5e66);"></div>
    <div class="product-tag" style="left:137px; top:435px;">Fitness Products</div>
  </section>
  <div class="banner-label" style="left:191px; top:540px;">1st Banner</div>

  <!-- Services banner -->
  <section class="banner banner-services">
    <div class="abs header" style="top:0;"></div>
    <div class="abs top-stripe"></div>
    <div class="brand" style="left:52px; top:22px; font-size:30px;"><span class="brand-dot" style="width:18px;height:18px;"></span>Vita Corner</div>

    <div class="photo octagon" role="img" aria-label="Blood pressure monitor with cuff" style="left:194px; top:106px; width:110px; height:168px; background:linear-gradient(135deg,var(--photo-device),#f6d2c8);"></div>

    <ul class="abs service-list">
      <li><svg class="tick" viewBox="0 0 10 10"><path d="M1 5.5l2.5 2.5L9 2" fill="none" stroke="#7dc242" stroke-width="1.8"/></svg>Private Consultation Area</li>
      <li><svg class="tick" viewBox="0 0 10 10"><path d="M1 5.5l2.5 2.5L9 2" fill="none" stroke="#7dc242" stroke-width="1.8"/></svg>Health Advice &amp; Information</li>
      <li><svg class="tick" viewBox="0 0 10 10"><path d="M1 5.5l2.5 2.5L9 2" fill="none" stroke="#7dc242" stroke-width="1.8"/></svg>Repeat Prescriptions</li>
      <li><svg class="tick" viewBox="0 0 10 10"><path d="M1 5.5l2.5 2.5L9 2" fill="none" stroke="#7dc242" stroke-width="1.8"/></svg>Blood Pressure Checks</li>
      <li><svg class="tick" viewBox="0 0 10 10"><path d="M1 5.5l2.5 2.5L9 2" fill="none" stroke="#7dc242" stroke-width="1.8"/></svg>Blood Sugar Tests</li>
      <li><svg class="tick" viewBox="0 0 10 10"><path d="M1 5.5l2.5 2.5L9 2" fill="none" stroke="#7dc242" stroke-width="1.8"/></svg>Contraception Advice</li>
    </ul>

    <div class="photo octagon" role="img" aria-label="Healthcare icons: doctor, heartbeat and checklist" style="left:-14px; top:268px; width:127px; height:132px; background:linear-gradient(135deg,var(--white) 0 14%,var(--photo-icons) 14% 100%);"></div>

    <div class="abs also-title">ALSO AVAILABLE</div>
    <ul class="abs extras">
      <li><svg class="tick" viewBox="0 0 10 10"><path d="M1 5.5l2.5 2.5L9 2" fill="none" stroke="#7dc242" stroke-width="1.8"/></svg>Reading Glasses</li>
      <li><svg class="tick" viewBox="0 0 10 10"><path d="M1 5.5l2.5 2.5L9 2" fill="none" stroke="#7dc242" stroke-width="1.8"/></svg>Medical Scrubs</li>
      <li><svg class="tick" viewBox="0 0 10 10"><path d="M1 5.5l2.5 2.5L9 2" fill="none" stroke="#7dc242" stroke-width="1.8"/></svg>Medical Supplies</li>
    </ul>
    <div class="abs open-small">OPEN 7 DAYS A WEEK</div>
    <div class="abs hours-small">Monday-Saturday 8:30am-7pm<br>Sunday 10am-2pm</div>

    <div class="photo octagon" role="img" aria-label="Red first aid kit" style="left:-10px; top:416px; width:115px; height:100px; background:linear-gradient(135deg,var(--white) 0 12%,var(--photo-kit) 12% 100%);"></div>
    <div class="abs insurance-band">WE ACCEPT ALL MAJOR INSURANCES</div>
  </section>
  <div class="banner-label" style="left:688px; top:540px;">2nd Banner</div>

  <!-- Opening hours banner -->
  <section class="banner banner-hours">
    <div class="abs header" style="top:0;"></div>
    <div class="brand" style="left:54px; top:22px; font-size:30px;"><span class="brand-dot" style="width:18px;height:18px;"></span>Vita Corner</div>
    <svg class="abs plus-ring" width="148" height="148" viewBox="0 0 148 148" aria-hidden="true">
      <circle cx="74" cy="74" r="66" fill="none" stroke="#ffffff" stroke-width="5"/>
      <rect x="36" y="64" width="76" height="20" fill="#7dc242"/>
      <rect x="64" y="36" width="20" height="76" fill="#7dc242"/>
    </svg>
    <div class="abs open-band">OPEN 7 DAYS A WEEK</div>
    <div class="abs hours-large">Monday-Saturday<br>8:30am-7pm<br>Sunday 10am-2pm</div>
    <div class="abs insurance-footer">WE ACCEPT ALL MAJOR INSURANCES</div>
  </section>
  <div class="banner-label" style="left:204px; top:1114px;">3rd Banner</div>

  <!-- Brand banner -->
  <section class="banner banner-brand">
    <div class="abs icon-field" role="img" aria-label="Faint pattern of medical icons: hospital beds, wheelchair, stethoscope, pills and thermometer"></div>
    <div class="brand" style="left:0; top:226px; width:287px; justify-content:center; font-size:34px; color:var(--white);"><span class="brand-dot" style="width:20px;height:20px;background:var(--white);"></span>Vita Corner</div>
  </section>
  <div class="banner-label" style="left:688px; top:1114px;">4th Banner</div>

</div>
</body>
</html>
```